RJ Penhall & Associates

Create a website encompassing design work already carried out for business card.
Small accounting practice, business accounting and management, superannuation, audit, taxation.

```html
<!DOCTYPE html>
<html lang="en">
<head>
<meta charset="utf-8">
<title>RJ Penhall &amp; Associates</title>
<link href="https://fonts.googleapis.com/css2?family=Roboto:wght@400;500&family=Open+Sans:wght@400;600&display=swap" rel="stylesheet">
<style>
:root{
  --dark:#1f1f1f;
  --darker:#161616;
  --blue:#6fa8dc;
  --blue-text:#4a8ccc;
  --heading:#2b2b2b;
  --body:#555;
  --muted:#6f6f6f;
  --rule:#d8d8d8;
  --white:#fff;
  --footer-text:#e6e6e6;
}
*{margin:0;padding:0;box-sizing:border-box}
html,body{width:897px;height:1200px;overflow:hidden;background:var(--white)}
body{position:relative;font-family:"Open Sans",Arial,sans-serif;color:var(--body)}
.abs{position:absolute}
h2,h3,.heading{font-family:"Roboto",Arial,sans-serif;font-weight:400;color:var(--heading)}

/* header */
.site-header{left:0;top:0;width:897px;height:62px;background:var(--dark)}
.brand{left:134px;top:13px;display:flex;align-items:center;gap:8px}
.brand-mark{width:30px;height:30px;background:var(--blue)}
.brand-name{font-family:"Roboto",sans-serif;font-weight:500;font-size:14px;line-height:15px;color:var(--white);width:110px}
.main-nav{top:29px;font-family:"Open Sans",sans-serif;font-size:8.5px;font-weight:600;color:var(--white);letter-spacing:.2px}
.main-nav.active{color:var(--blue)}
.service-strip{left:0;top:62px;width:897px;height:19px;background:var(--blue);font-family:Arial,sans-serif;font-weight:bold;font-size:7px;color:var(--white);padding:5px 0 0 137px}

/* hero */
.hero{left:0;top:81px;width:897px;height:342px;background:var(--dark)}
.slide{left:135px;top:97px;width:628px;height:278px;background:var(--white);padding:5px}
.slide-photo{width:100%;height:100%;background:linear-gradient(135deg,#dfe6ee 0%,#c9d6e4 40%,#eef1f4 70%,#b8c9da 100%)}
.slide-caption{left:161px;top:307px;width:272px;height:43px;background:rgba(255,255,255,.7);font-family:"Roboto",sans-serif;font-size:19px;color:#333;padding:9px 0 0 20px}
.dots{left:428px;top:397px;display:flex;gap:6px}
.dot{width:8px;height:8px;border-radius:50%;background:var(--white)}
.dot.hollow{background:transparent;border:1.5px solid var(--white)}

/* propositions */
.section-title{font-size:16px}
.prop-photo{width:148px;height:93px;border:1px solid #ccc;padding:2px;background:var(--white)}
.prop-photo div{width:100%;height:100%}
.prop-title{font-family:"Roboto",sans-serif;font-size:12px;line-height:16px;color:var(--heading);width:150px}
.prop-text{font-size:8px;line-height:15.5px;color:var(--body);width:150px}
.dash{left:138px;width:621px;border-top:1px dashed #c8c8c8}

.welcome-text{left:135px;top:709px;width:405px;font-size:8px;line-height:15.3px;color:var(--body)}
.video{left:556px;top:687px;width:207px;height:117px;background:linear-gradient(120deg,#a9c8e6 0%,#e9eef3 55%,#cfd8e0 100%)}
.play{left:636px;top:728px}

.col{width:196px}
.col h3{font-size:16px;margin-bottom:9px}
.col .lead{font-size:9px;line-height:15.5px;color:#333;margin-bottom:5px}
.col .detail{font-size:8px;line-height:15.5px;color:var(--muted);padding-bottom:8px;border-bottom:1px solid var(--rule)}
.more{width:53px;height:25px;background:var(--blue);color:var(--white);font-family:"Roboto",sans-serif;font-size:9px;text-align:center;line-height:25px}
.author{font-family:"Roboto",sans-serif;font-size:9px;color:var(--blue-text);margin-top:6px}
.author-role{font-size:8px;color:#333;margin-top:2px}
.arrows{left:741px;top:845px;display:flex;gap:4px}

/* footer */
.site-footer{left:0;top:1028px;width:897px;height:124px;background:var(--dark)}
.footer-title{font-family:"Roboto",sans-serif;font-size:12px;color:var(--white)}
.footer-list{font-size:8px;line-height:19.2px;color:var(--footer-text);list-style:none}
.footer-list li{display:flex;align-items:center;gap:4px}
.social-box{width:9px;height:9px;display:inline-block}
.email-field{left:135px;top:1073px;width:130px;height:28px;background:var(--white);font-size:7.5px;color:#999;padding:9px 6px}
.subscribe{left:135px;top:1108px;width:78px;height:24px;background:var(--blue);color:var(--white);font-size:9px;text-align:center;line-height:24px}
.world-map{left:640px;top:1068px;width:125px;height:75px;background:radial-gradient(ellipse at center,#3a3a3a 0%,rgba(40,40,40,0) 70%)}
.contact-row{display:flex;gap:5px;font-size:8px;line-height:11.5px;color:var(--footer-text)}
.bottom-bar{left:0;top:1152px;width:897px;height:48px;background:var(--darker);font-size:8px;color:var(--footer-text)}
</style>
</head>
<body>

<header class="abs site-header">
  <div class="abs brand"><span class="brand-mark"></span><span class="brand-name">RJ Penhall &amp; Associates</span></div>
  <span class="abs main-nav active" style="left:423px">HOME</span>
  <span class="abs main-nav" style="left:491px">SERVICES</span>
  <span class="abs main-nav" style="left:571px">PROJECTS</span>
  <span class="abs main-nav" style="left:653px">CONTACTS</span>
  <span class="abs main-nav" style="left:740px">BLOG</span>
</header>
<div class="abs service-strip">Accountant · Business Solutions · Management · Superannuation · Audit</div>

<section class="abs hero"></section>
<div class="abs slide"><div class="slide-photo" role="img" aria-label="Smiling team of accountants around a meeting table in a bright office"></div></div>
<div class="abs slide-caption">Small Accounting Practice</div>
<div class="abs dots"><span class="dot"></span><span class="dot hollow"></span><span class="dot"></span></div>

<h2 class="abs section-title" style="left:135px;top:442px">Our Best Propositions for You!</h2>

<div class="abs prop-photo" style="left:135px;top:472px"><div role="img" aria-label="Hand at a calculator with money in the sky" style="background:linear-gradient(160deg,#4f86c6,#c8dcef 60%,#9aa3ad)"></div></div>
<div class="abs prop-title" style="left:135px;top:571px">Business Accounting and Management</div>
<div class="abs prop-text" style="left:135px;top:605px">Lorem ipsum dolor sit amet, consect etuer adipiscing elit, sed diam no nummy nibh.</div>

<div class="abs prop-photo" style="left:295px;top:472px"><div role="img" aria-label="Piggy bank in grass under a blue sky" style="background:linear-gradient(180deg,#3f7fc8,#d8e6f2 55%,#7fb04a)"></div></div>
<div class="abs prop-title" style="left:295px;top:571px">Superannuation</div>
<div class="abs prop-text" style="left:295px;top:591px">Lorem ipsum dolor sit amet, consect etuer adipiscing elit, sed diam no nummy nibh.</div>

<div class="abs prop-photo" style="left:455px;top:472px"><div role="img" aria-label="Hands reviewing financial charts with a pen" style="background:linear-gradient(135deg,#2a2f3a,#9fb6cc 50%,#e6ecf2)"></div></div>
<div class="abs prop-title" style="left:455px;top:571px">Audit</div>
<div class="abs prop-text" style="left:455px;top:591px">Lorem ipsum dolor sit amet, consect etuer adipiscing elit, sed diam no nummy nibh.</div>

<div class="abs prop-photo" style="left:615px;top:472px"><div role="img" aria-label="Calculator and pen on tax papers" style="background:linear-gradient(135deg,#6e8299,#b9c8d8 55%,#e4eaf0)"></div></div>
<div class="abs prop-title" style="left:615px;top:571px">Taxation</div>
<div class="abs prop-text" style="left:615px;top:591px">Lorem ipsum dolor sit amet, consect etuer adipiscing elit, sed diam no nummy nibh.</div>

<div class="abs dash" style="top:665px"></div>

<h2 class="abs section-title" style="left:135px;top:683px">Welcome To RJ Penhall</h2>
<p class="abs welcome-text">Ut wisi enim ad minim veniam, quis nostrud exerci tation ullamcorper suscipit lobortis nisl ut aliquip ex ea commodo consequat. Duis autem vel eum iriure dolor in hendrerit in vulputate velit esse molestie consequat, vel illum dolore eu feugiat nulla facilisis at vero eros et accumsan et iusto odio dignissim qui blandit praesent luptatum zzril delenit augue duis dolore te feugait nulla facilisi.<br>Nam liber tempor cum soluta nobis eleifend option congue nihil imperdiet doming id quod mazim placerat facer possim assum.</p>
<div class="abs video" role="img" aria-label="Video still of hands writing beside a calculator"></div>
<svg class="abs play" width="36" height="36" viewBox="0 0 36 36"><circle cx="18" cy="18" r="17" fill="#e05a5a" opacity=".8"/><path d="M14 11 L26 18 L14 25 Z" fill="#fff"/></svg>

<div class="abs dash" style="top:819px"></div>

<div class="abs col" style="left:135px;top:838px">
  <h3>Why Us</h3>
  <p class="lead">Lorem ipsum dolor sit amet, consectetuer adipiscing elit, sed diam nonummy</p>
  <p class="detail">Ut wisi enim ad minim veniam, quis nostrud exerci tation ullamcorper suscipit lobortis nisl ut aliquip ex ea commodo consequat.</p>
</div>
<div class="abs more" style="left:135px;top:964px">MORE</div>

<div class="abs col" style="left:351px;top:838px">
  <h3>Strategies</h3>
  <p class="lead">Typi non habent claritatem insitam; est usus legentis in iis qui facit eorum claritatem.</p>
  <p class="detail">Ut wisi enim ad minim veniam, quis nostrud exerci tation ullamcorper suscipit lobortis nisl ut aliquip ex ea commodo consequat.</p>
</div>
<div class="abs more" style="left:351px;top:964px">MORE</div>

<div class="abs col" style="left:567px;top:838px">
  <h3>Testmonials</h3>
  <p class="lead">Eodem modo typi, qui nunc nobis videntur parum clari, fiant sollemnes in futurum.</p>
  <p class="detail">Mirum est notare quam littera gothica, quam nunc putamus parum claram, anteposuerit littera rum formas humanitatis.</p>
  <p class="author">MARA LENT</p>
  <p class="author-role">Aipisicing elit, sed do eiusmod</p>
</div>
<svg class="abs arrows" width="22" height="9" viewBox="0 0 22 9"><circle cx="4.5" cy="4.5" r="4.5" fill="#777"/><path d="M5.5 2.5 L3 4.5 L5.5 6.5Z" fill="#fff"/><circle cx="17.5" cy="4.5" r="4.5" fill="var(--blue)"/><path d="M16.5 2.5 L19 4.5 L16.5 6.5Z" fill="#fff"/></svg>

<footer class="abs site-footer"></footer>
<div class="abs footer-title" style="left:135px;top:1047px">Newsletter</div>
<div class="abs email-field">Email Address</div>
<div class="abs subscribe">Subscribe</div>

<div class="abs footer-title" style="left:315px;top:1047px">Help &amp; Support</div>
<ul class="abs footer-list" style="left:315px;top:1063px"><li>FAQ's</li><li>Live Support</li><li>Send Mail</li></ul>

<div class="abs footer-title" style="left:447px;top:1047px">Social Connection</div>
<ul class="abs footer-list" style="left:447px;top:1063px">
  <li><span class="social-box" style="background:#3b5998"></span>Facelink</li>
  <li><span class="social-box" style="background:#3fa9dd"></span>Chirper</li>
  <li><span class="social-box" style="background:#d34836"></span>Circles +</li>
  <li><span class="social-box" style="background:#f08a24"></span>RSS</li>
</ul>

<div class="abs world-map" role="img" aria-label="Faint world map"></div>
<div class="abs footer-title" style="left:610px;top:1047px">Get In touch</div>
<div class="abs contact-row" style="left:612px;top:1071px">
  <svg width="8" height="9" viewBox="0 0 8 9"><path d="M1 0.5 L3 0.5 L3.5 2.5 L2.5 3.3 Q3.5 5.5 5 6.2 L5.8 5.2 L7.8 5.8 L7.5 8 Q3 8 0.5 2.5Z" fill="#fff"/></svg>
  <span>+(01)-55-210-347-6</span></div>
<div class="abs contact-row" style="left:612px;top:1096px">
  <svg width="10" height="8" viewBox="0 0 10 8"><rect x=".5" y=".5" width="9" height="7" fill="none" stroke="#fff"/><path d="M.5 .5 L5 4.5 L9.5 .5" fill="none" stroke="#fff"/></svg>
  <span>info@rjpenhall.com</span></div>
<div class="abs contact-row" style="left:613px;top:1118px">
  <svg width="8" height="10" viewBox="0 0 8 10"><path d="M4 0 A3.8 3.8 0 0 1 7.8 3.8 Q7.8 6 4 10 Q0.2 6 0.2 3.8 A3.8 3.8 0 0 1 4 0Z" fill="#fff"/><circle cx="4" cy="3.8" r="1.4" fill="#1f1f1f"/></svg>
  <span>38 lorem ipsm2 rd, lorem ipsm,<br>lorem ipsm, lorem ipsm 10250</span></div>

<div class="abs bottom-bar">
  <span class="abs" style="left:135px;top:19px">Sitemap &nbsp;|&nbsp; Privacy &amp; policy</span>
  <span class="abs" style="left:591px;top:19px">Copyright 2014 RJ Penhall. All rights reserved.</span>
</div>

</body>
</html>
```